Work Van Graphics Design

Use the attached logo and design a work van.  The van should be orange (the same orange in the attached logo) and the logo and text will be white.  I want the text to be big and bold, the same hight as the graphic in the logo.  The text should be "BRAMLEY HOUSE CREW'S" instead of just Bramley.
The other text that needs to be on the van somewhere:
www.BramleyHouseCrew.example
614-555-0182
Roofing
Plumbing
Water Restoration
Carpet Cleaning
Window Cleaning
HVAC

```html
<!DOCTYPE html>
<html lang="en">
<head>
<meta charset="utf-8">
<title>Bramley House Crew's – Work Van Graphics</title>
<link rel="stylesheet" href="https://fonts.googleapis.com/css2?family=Jost:wght@400;500&display=swap">
<style>
  :root {
    --van-orange: #f28a1f;
    --wrap-white: #ffffff;
  }
  * { margin: 0; padding: 0; box-sizing: border-box; }
  html, body {
    width: 1200px;
    height: 594px;
    overflow: hidden;
    background: var(--van-orange);
  }
  .van-wrap {
    position: relative;
    width: 1200px;
    height: 594px;
    background: var(--van-orange);
    color: var(--wrap-white);
    font-family: "Jost", "Century Gothic", sans-serif;
    font-weight: 400;
  }
  .brand-mark {
    position: absolute;
    left: 664px;
    top: 168px;
    width: 82px;
    height: 82px;
    background: var(--wrap-white);
  }
  .brand-name {
    position: absolute;
    left: 760px;
    top: 164px;
    font-size: 50px;
    line-height: 52px;
    font-weight: 500;
    white-space: nowrap;
  }
  .brand-name span { display: block; }
  .brand-name .brand-first {
    letter-spacing: 0.255em;
  }
  .brand-name .brand-second {
    letter-spacing: 0.01em;
  }
  .services {
    position: absolute;
    left: 390px;
    top: 298px;
    list-style: none;
    font-size: 18px;
    line-height: 24.3px;
  }
  .services li::before {
    content: "";
    display: inline-block;
    width: 4px;
    height: 4px;
    border-radius: 50%;
    background: var(--wrap-white);
    margin: 0 7px 3px 0;
    vertical-align: middle;
  }
  .website {
    position: absolute;
    left: 648px;
    top: 302px;
    font-size: 31px;
    letter-spacing: 0;
    white-space: nowrap;
  }
  .phone {
    position: absolute;
    left: 597px;
    top: 380px;
    font-size: 46px;
    letter-spacing: 0.01em;
    white-space: nowrap;
  }
</style>
</head>
<body>
  <main class="van-wrap">
    <div class="brand-mark" aria-hidden="true"></div>
    <h1 class="brand-name"><span class="brand-first">BRAMLEY</span><span class="brand-second">HOUSE CREW'S</span></h1>
    <ul class="services">
      <li>Roofing</li>
      <li>Plumbing</li>
      <li>Water Restoration</li>
      <li>Carpet Cleaning</li>
      <li>Window Cleaning</li>
      <li>HVAC</li>
    </ul>
    <p class="website">www.BramleyHouseCrew.example</p>
    <p class="phone">614-555-0182</p>
  </main>
</body>
</html>
```